hotel's Website

Hotels website redesign for reference pictures, logo etc see http://restwellmarlow.co.uk/

1. 2-3 Special offers on the main page.
2. Booking calender
3. Location Map
4. Picture gallery.
5. Journeyscope reviews.
6. short description
7. Social Media sharing.
8 Phone number and address.

Industry/Entity Type

Hotel

Requirements
Must have
• 1. 2-3 Special offers on the main page.
2. Booking calender
3. Location Map
4. Picture gallery.
5. Journeyscope reviews.
6. short description
7. Social Media sharing.

```html
<!DOCTYPE html>
<html lang="en">
<head>
<meta charset="utf-8">
<title>Restwell Inn Marlow - Riverside</title>
<link rel="stylesheet" href="https://fonts.googleapis.com/css2?family=Roboto+Condensed:wght@400;500&family=Source+Sans+3:wght@300;400;600&display=swap">
<style>
:root{
  --header-dark:#333d47;
  --header-stripe:#2d363f;
  --orange:#ff9d0a;
  --orange-light:#ffb52e;
  --orange-border:#e57f00;
  --teal:#3a9fc4;
  --teal-light:#5ab8d9;
  --navy:#1f4e6b;
  --heading:#2f3a44;
  --text:#6b737a;
  --card-title:#2a8bbf;
  --footer-bg:#eef0f2;
  --footer-bottom:#dfe2e5;
  --white:#ffffff;
}
*{margin:0;padding:0;box-sizing:border-box}
html,body{width:856px;height:1200px;overflow:hidden;background:var(--white)}
body{position:relative;font-family:"Source Sans 3",sans-serif;color:var(--text)}
.abs{position:absolute}

.site-header{left:0;top:0;width:856px;height:122px;background:repeating-linear-gradient(135deg,var(--header-dark) 0 3px,var(--header-stripe) 3px 5px)}
.brand{left:94px;top:16px;width:43px;height:43px;background:#1b6fb5;border-radius:2px}
.brand-name{left:78px;top:62px;font-size:8px;letter-spacing:2px;color:#c7cdd3;text-transform:uppercase}
.brand-title{left:92px;top:26px;width:60px;font-size:9px;font-weight:600;color:var(--white);text-align:center;line-height:1.1}
.brand-divider{left:164px;top:16px;width:1px;height:47px;background:#7b858e}
.brand-location{left:175px;top:32px;font-size:14px;color:var(--white);font-family:"Source Sans 3",sans-serif}
.call-label{right:172px;top:38px;font-size:10px;color:#9aa3ac;letter-spacing:.3px}
.call-number{right:171px;top:51px;font-size:16px;color:var(--white)}
.lang{left:696px;top:39px;width:78px;height:26px;border:1px solid #4d5761;background:#3a444e;display:flex;align-items:center;padding-left:9px;gap:5px;font-size:11px;color:var(--white)}
.lang-flag{width:19px;height:12px;background:#2a4a8c;border:1px solid #d8dde2}
.lang-caret{width:0;height:0;border-left:4px solid transparent;border-right:4px solid transparent;border-top:5px solid #9aa3ac;margin-left:4px}

.main-nav{left:70px;top:88px;width:713px;height:35px;background:linear-gradient(var(--orange-light),var(--orange));display:flex;border-bottom:1px solid var(--orange-border)}
.main-nav a{font-family:"Roboto Condensed",sans-serif;font-size:13px;color:var(--white);text-decoration:none;display:flex;align-items:center;justify-content:center;border-right:1px solid #e58c00;height:100%}
.main-nav a:last-child{border-right:none}

.hero{left:70px;top:122px;width:713px;height:300px;background:linear-gradient(100deg,#3a332c 0%,#8b7b6a 28%,#e0c23a 45%,#d2cbc2 62%,#c9b38c 80%,#b48f55 100%)}
.booking{left:558px;top:170px;width:200px;height:214px;background:rgba(72,172,208,.88);border:2px solid rgba(180,225,240,.7);border-radius:3px;padding:20px 17px 0}
.booking h2{font-family:"Roboto Condensed",sans-serif;font-weight:400;font-size:21px;color:var(--white)}
.booking p{font-size:8px;line-height:14px;color:#0f3b52;margin-top:2px}
.booking label{display:block;font-size:9px;color:#0f3b52;margin-top:7px}
.booking .field{height:19px;background:var(--white);border-radius:2px;font-size:8px;color:#6b737a;padding:4px 9px;margin-top:3px}
.booking .search{position:absolute;right:16px;bottom:28px;height:20px;padding:0 10px;background:var(--navy);border-radius:3px;font-family:"Roboto Condensed",sans-serif;font-size:9px;color:var(--white);display:flex;align-items:center}
.slider-dots{left:401px;top:403px;display:flex;gap:3px}
.slider-dots span{width:11px;height:11px;border-radius:50%;background:var(--white)}
.slider-dots span:first-child{background:#5f666d}

.intro{left:0;top:452px;width:856px;text-align:center}
.intro h1{font-weight:300;font-size:26px;color:var(--heading)}
.intro h3{font-weight:300;font-size:18px;color:var(--heading);margin-top:2px}
.intro p{font-weight:300;font-size:10px;line-height:15px;color:var(--text);width:600px;margin:10px auto 0}
.btn{top:560px;height:26px;font-family:"Roboto Condensed",sans-serif;font-size:11px;color:var(--white);display:flex;align-items:center;justify-content:center}
.btn-gallery{left:333px;width:90px;background:linear-gradient(var(--orange-light),var(--orange));border-bottom:2px solid var(--orange-border)}
.btn-learn{left:430px;width:82px;background:linear-gradient(var(--teal-light),var(--teal));border-bottom:2px solid #2a82a6}
.intro-rule{left:78px;top:614px;width:700px;height:1px;background:linear-gradient(90deg,transparent,#e4e7ea 20%,#e4e7ea 80%,transparent)}

.card{top:650px;width:214px;height:224px;border:1px solid #e1e4e7;background:linear-gradient(#fff 60%,#f3f4f5)}
.card-photo{height:100px}
.card h4{font-family:"Roboto Condensed",sans-serif;font-weight:400;font-size:16px;color:var(--card-title);margin:11px 0 0 18px}
.card p{font-weight:300;font-size:8.5px;line-height:14px;color:var(--text);margin:3px 12px 0 18px}
.card .more{display:block;font-family:"Roboto Condensed",sans-serif;font-size:9px;color:#222;margin:9px 0 0 20px}

.footer{left:0;top:930px;width:856px;height:220px;background:linear-gradient(#e6e9ec,var(--footer-bg) 12px)}
.footer-col{top:965px}
.footer-col h5{font-family:"Roboto Condensed",sans-serif;font-weight:400;font-size:15px;color:var(--heading)}
.footer-col p,.footer-col li{font-size:9px;line-height:15px;color:#3b444c}
.footer-col p{margin-top:8px}
.footer-col ul{list-style:none;margin-top:7px}
.footer-sep{top:966px;width:1px;height:132px;background:#d6dadd}
.review-badge{margin-top:8px;width:174px;height:37px;background:#000;border-radius:4px;display:flex;align-items:center;padding-left:10px;gap:7px;font-size:17px;color:var(--white)}
.review-badge i{width:14px;height:14px;border-radius:50%;background:var(--white);display:block}
.newsletter-input{margin-top:9px;width:173px;height:21px;background:var(--white);border:1px solid #cfd4d8;font-size:8px;color:#9aa1a7;padding:5px 8px}
.subscribe{margin:7px 0 0 104px;width:69px;height:22px;background:linear-gradient(var(--teal-light),var(--teal));border-radius:2px;font-family:"Roboto Condensed",sans-serif;font-size:10px;color:var(--white);display:flex;align-items:center;justify-content:center}
.social{display:flex;gap:6px;margin:9px 0 0 84px}
.social span{width:17px;height:17px;border-radius:2px}
.footer-bottom{left:0;top:1150px;width:856px;height:50px;background:var(--footer-bottom)}
.copyright{left:75px;top:1170px;font-size:9px;color:#6b737a}
</style>
</head>
<body>

<header class="site-header abs"></header>
<div class="brand abs"></div>
<div class="brand-title abs">Restwell<br>Inn</div>
<div class="brand-name abs">by Harbourline Hotels</div>
<div class="brand-divider abs"></div>
<div class="brand-location abs">Marlow - Riverside</div>
<div class="call-label abs">CALL US NOW</div>
<div class="call-number abs">+44 (0) 20 7946 0123</div>
<div class="lang abs"><span class="lang-flag"></span>English<span class="lang-caret"></span></div>

<nav class="main-nav abs">
  <a style="width:70px">HOME</a>
  <a style="width:88px">OUR ROOMS</a>
  <a style="width:93px">ATTRACTIONS</a>
  <a style="width:114px">LONDON EVENTS</a>
  <a style="width:107px">SPECIAL OFFERS</a>
  <a style="width:69px">PHOTOS</a>
  <a style="width:87px">DIRECTIONS</a>
  <a style="width:85px">CONTACT</a>
</nav>

<div class="hero abs" role="img" aria-label="Bright hotel lounge with a yellow armchair, grey sofa with colourful cushions and a round glass table"></div>
<form class="booking abs">
  <h2>BOOK A ROOM</h2>
  <p>Cum sociis natoque penatibus et magnis dis parturient montes, nascetur ridiculus</p>
  <label>From to</label>
  <div class="field">October 30, 2013</div>
  <label>To</label>
  <div class="field">October 31, 2013</div>
  <div class="search">SEARCH NOW</div>
</form>
<div class="slider-dots abs"><span></span><span></span><span></span><span></span></div>

<section class="intro abs">
  <h1>Duis tincidunt lectus quis dui viverra vestibulum</h1>
  <h3>Suspendisse vulputate aliquam dui Nulla elementum dui ut augue Aliquam vehicula</h3>
  <p>Mauris vel lacus vitae felis vestibulum volutpat. Etiam est nunc, venenatis in, tristique eu, imperdiet ac, nisl. Cum sociis natoque penatibus et magnis dis parturient montes, nascetur ridiculus mus. In iaculis facilisis massa. Etiam eu urna. Sed porta. Suspendisse quam leo</p>
</section>
<a class="btn btn-gallery abs">VIEW GALLERY</a>
<a class="btn btn-learn abs">LEARN MORE</a>
<div class="intro-rule abs"></div>

<article class="card abs" style="left:88px">
  <div class="card-photo" role="img" aria-label="Clock tower and parliament at night with light trails" style="background:linear-gradient(120deg,#1d3a6e,#3f6fb0 40%,#c98a2a 70%,#f2c24a)"></div>
  <h4>SPECIAL OFFERS</h4>
  <p>Enjoy your stay at Restwell Inn Marlow and be sure that you've found our best value on the Internet. We always have some exclusive special offers for our guests.</p>
  <span class="more">LEARN MORE</span>
</article>
<article class="card abs" style="left:321px">
  <div class="card-photo" role="img" aria-label="Riverside skyline at dusk with an illuminated observation wheel" style="background:linear-gradient(#6b4a7c,#b3738a 45%,#3a2a3e 75%,#1d1a24)"></div>
  <h4>EXPLORE LONDON</h4>
  <p>Enjoy your stay at Restwell Inn Marlow and be sure that you've found our best value on the Internet. We always have some exclusive special offers for our guests.</p>
  <span class="more">LEARN MORE</span>
</article>
<article class="card abs" style="left:553px">
  <div class="card-photo" role="img" aria-label="Hotel bedroom with a made bed, red throw and wooden headboard" style="background:linear-gradient(110deg,#e9e2d4,#c79a4e 40%,#e2c48a 65%,#f1ede6)"></div>
  <h4>STAY IN COMFORT</h4>
  <p>Enjoy your stay at Restwell Inn Marlow and be sure that you've found our best value on the Internet. We always have some exclusive special offers for our guests.</p>
  <span class="more">LEARN MORE</span>
</article>

<footer class="footer abs"></footer>
<div class="footer-sep abs" style="left:289px"></div>
<div class="footer-sep abs" style="left:528px"></div>

<div class="footer-col abs" style="left:75px;width:190px">
  <h5>PARTNER HOTEL</h5>
  <p>This hotel is owned and operated by the 5K Hotel Group, please take a look of some of our other hotels below:</p>
  <ul>
    <li>Hollybrook Inn - Camden Lock</li>
    <li>Hollybrook Express - Earls Court</li>
    <li>Centrepoint House Hotel</li>
    <li>Simplestay Victoria</li>
  </ul>
</div>
<div class="footer-col abs" style="left:315px;width:200px">
  <h5>JOURNEYSCOPE</h5>
  <div class="review-badge"><i></i>Journeyscope</div>
  <p>Stayed with us before? Want to view experiences from our previous guests? Read reviews on our Journeyscope page.</p>
</div>
<div class="footer-col abs" style="left:560px;width:190px">
  <h5>STAY IN TOUCH</h5>
  <p>Sign up for our newsletter for latest news from Restwell Inn Marlow - Riverside</p>
  <div class="newsletter-input">email address</div>
  <div class="subscribe">SUBSCRIBE</div>
  <div class="social">
    <span style="background:#3b5b9a"></span>
    <span style="background:#5ab8e6"></span>
    <span style="background:#1a6fa8"></span>
    <span style="background:#f08a1c"></span>
  </div>
</div>

<div class="footer-bottom abs"></div>
<div class="copyright abs">© 2013 Company Name.&nbsp; All right reserved</div>

</body>
</html>
```